Event website for the Brisk industry

brisk! is a new show in the Australian market so the website needs to be informative, easy to navigate and clear as to what the event is about and why they should attend – needs to be professional but still fun and dynamic.

Imagery needs to be colourful, fresh, inviting, and should involve a mixture of close up food shots with shots of people interacting.
The event’s competitions are fun and a little quirky (the “Toastathon” and “Blender Contest”), so creative should represent this in tone.

brisk! is a niche and unique show aimed at the multi-million dollar food-to-go market in Australia.
Key selling points for visitors:
- Discover the latest products (food and beverage lines) and equipment to hit the market
- Network with their peers
- Immerse themselves in a range of fun and interactive features – see attached list.
Key selling points for exhibitors:
- Speak directly to decision makers from small – large, food to go related businesses.
- Small niche show, exhibitors have more of an opportunity to stand out/ limited size so good variety of products on display

Some examples of Australian websites which are targeting the same type of customer:
http://www.wrapguild.org.au/ - clean/bright/simple
www.platterexpoaus.com.au – we like the simplicity of the Platter Expo website – very clean/colourful.
Updates

Hi All, 

Thanks for the interest in our competition, I will be away until the 11th of January at which point i will comment on the designs. 

Thanks and Merry Xmas. 

Target Market(s)

Café/Restaurant owners Sandwich bars/Juice Bars/Bakeries/Delis/Gourmet food stores Pubs/Clubs/Contract Caterers Supermarkets/Food Wholesalers

Industry/Entity Type

Industry

Requirements
Must have
• Main objectives:
1. Visitor Registration – call to action to "Register Now" needs to be very prominent on the home page and on the pages throughout the website
2. Information on exhibiting "Want to Exhibit" – needs to be clearly available.
3. Being a new show, data capture is important, so this needs to feature on the home page.
4. Social Media share buttons
5. Floating CSS Nav bar (top or bottom) with key call to actions - Register, Want to exhibit?, sign up

I would like all designs to have both a home page and a content page submitted.
Should not have
• Brisk UK show website: www.briskshow.co.uk
- We will be using the same branding as the UK brisk show website but we don’t like how busy their website is (too many blocks of run on text and too many navigation tiles on the home page). We would prefer to take a more simplified approach – ie. hero images (JQuery) dominating the screen, with a really strong CTA to register and to find out more about exhibiting.

```html
<!DOCTYPE html>
<html lang="en">
<head>
<meta charset="utf-8">
<title>brisk! – the contemporary food to go show</title>
<link href="https://fonts.googleapis.com/css2?family=Didact+Gothic&display=swap" rel="stylesheet">
<style>
:root{
  --ink:#1a1a1a;
  --muted:#8a8a8a;
  --rule:#cfcfcf;
  --yellow:#f7e21a;
  --yellow-deep:#e8c800;
  --white:#ffffff;
  --search:#efefef;
  --social:#2f6fb0;
}
*{margin:0;padding:0;box-sizing:border-box}
html,body{width:1200px;height:802px;overflow:hidden;background:var(--white)}
body{position:relative;font-family:"Didact Gothic",sans-serif;color:var(--ink)}
.abs{position:absolute}
.brand{left:31px;top:35px;width:128px;height:86px;display:flex;align-items:center;gap:8px}
.brand-mark{width:14px;height:14px;background:var(--ink)}
.brand-name{font-size:34px;color:var(--ink);line-height:1}
.nav-head{font-size:12.5px;text-transform:uppercase;color:var(--ink)}
.nav-list{list-style:none}
.nav-list li{font-size:12.5px;text-transform:uppercase;color:var(--muted);height:17.5px;line-height:17.5px;letter-spacing:.3px}
.nav-list li.strong{color:var(--ink)}
.search{left:959px;top:35px;width:210px;height:24px;background:var(--search);font-size:11px;color:#c4c4c4;padding:6px 7px;text-transform:uppercase}
.register{left:940px;top:90px;width:120px;height:120px;border-radius:50%;
  background:radial-gradient(circle at 40% 35%,#fff36a,var(--yellow) 55%,var(--yellow-deep));
  box-shadow:0 3px 6px rgba(0,0,0,.3),inset 0 0 0 3px #fff8a0;
  display:flex;align-items:center;justify-content:center;text-align:center;
  font-size:21px;line-height:1.05;text-transform:uppercase;transform:rotate(10deg)}
.rule{left:31px;width:1138px;height:1px;background:var(--rule)}
.hero{left:31px;top:261px;width:1138px;height:457px;overflow:hidden;
  background:linear-gradient(100deg,#e9e4e7 0%,#e6e0e3 22%,#d9b79a 42%,#e9a263 58%,#f1e6d6 72%,#e8e2e4 100%)}
.hero-date{left:49px;top:38px;font-size:35px;letter-spacing:.5px}
.venue{left:78px;top:92px;font-family:Arial,sans-serif;font-size:12.5px;line-height:17.5px}
.stem{width:1px;background:#4a4a4a}
.tag{background:var(--white);font-size:12.5px;text-transform:uppercase;padding:0 8px;height:25px;line-height:25px}
.pitch{background:var(--yellow);font-size:12.5px;text-transform:uppercase;padding:6px 8px;line-height:17.5px}
.footer-copy{left:31px;top:750px;font-family:Arial,sans-serif;font-size:11.5px;color:#333}
.social{width:26px;height:26px;border-radius:50%;background:var(--social);top:744px}
.footer-links{left:979px;top:750px;display:flex;gap:14px;font-size:13px;color:#333}
</style>
</head>
<body>
  <div class="abs brand"><span class="brand-mark"></span><span class="brand-name">brisk!</span></div>

  <nav>
    <div class="abs nav-head" style="left:271px;top:55px">Exhibiting</div>
    <ul class="abs nav-list" style="left:311px;top:70px">
      <li>Who exhibits?</li><li>Who will you meet?</li><li>Exhibitor brochure 2012</li><li>Floorplan and rates</li><li class="strong">Want to exhibit</li>
    </ul>
    <div class="abs nav-head" style="left:524px;top:55px">Visiting</div>
    <ul class="abs nav-list" style="left:545px;top:70px">
      <li>Who should visit?</li><li>Education at brisk!</li><li>Exhibitor show highlights</li><li>brisk! survery 2012</li>
    </ul>
    <div class="abs nav-head" style="left:750px;top:55px">Contact us</div>
  </nav>

  <div class="abs search">Search</div>
  <div class="abs register">Register<br>now!</div>

  <div class="abs rule" style="top:245px"></div>

  <section class="abs hero">
    <div class="abs" role="img" aria-label="Close-up photo of seared scallops, prawns and fish with micro greens on a white plate" style="inset:0"></div>
    <div class="abs hero-date">6-7 AUGUST 2012</div>
    <div class="abs venue">Grand Hall of Trades<br>Elm Park<br>Sydney</div>

    <div class="abs stem" style="left:234px;top:144px;height:313px"></div>
    <div class="abs tag" style="left:235px;top:224px">Discover</div>
    <div class="abs pitch" style="left:235px;top:256px;width:155px">The latest products<br>and equipment<br>to hit the market</div>

    <div class="abs stem" style="left:569px;top:-16px;height:473px"></div>
    <div class="abs tag" style="left:570px;top:79px">Network</div>
    <div class="abs pitch" style="left:570px;top:110px;width:125px;padding-top:4px;padding-bottom:4px">With your peers</div>

    <div class="abs stem" style="left:867px;top:189px;height:268px"></div>
    <div class="abs tag" style="left:868px;top:224px">Interact</div>
    <div class="abs pitch" style="left:868px;top:256px;width:165px">Immerse yourself<br>amongst a range of<br>interactive features</div>
  </section>

  <div class="abs rule" style="top:730px"></div>

  <footer>
    <div class="abs footer-copy">Copyright © 2012. brisk!</div>
    <div class="abs social" style="left:898px"></div>
    <div class="abs social" style="left:939px"></div>
    <div class="abs footer-links"><span>Home</span><span>Legal</span><span>Privacy</span><span>Contact</span></div>
  </footer>
</body>
</html>
```